LMVBeacon online header

We need a header for our online internal company newsletter/blogsite. It is called the LMVBeacon which is a contraction between LMV (the department associated) and the word Gazette.
We want to have a new modern design for the header that should say "LMVBeacon" or "LMVBeacon online" (there used to be a paper version) in a nice artistic modern friendly inviting way. Sort of like a newspaper header.
There could be an optional text line that says "All the news you need" or something like that.
Target Market(s)
Consulting professionals in the area of mathematics, econometrics and IT
Industry/Entity Type
It Company
Logo Text
LMVBeacon
Colors
Designer to choose colors to be used in the design.
Look and feel

```html
<!DOCTYPE html>
<html lang="en">
<head>
<meta charset="utf-8">
<title>LMVBeacon — All the news you need</title>
<link rel="stylesheet" href="https://fonts.googleapis.com/css2?family=Alegreya:wght@700&display=swap">
<style>
  :root {
    --parchment-light: #ece4d1;
    --parchment-mid: #e0d5bc;
    --parchment-dark: #cfc1a3;
    --ink: #121110;
    --rule: #1c1a17;
  }
  html, body {
    margin: 0;
    padding: 0;
    width: 1200px;
    height: 368px;
    overflow: hidden;
    background: var(--parchment-mid);
  }
  .masthead {
    position: relative;
    width: 1200px;
    height: 368px;
    overflow: hidden;
  }
  .masthead__backdrop {
    position: absolute;
    inset: 0;
    background: radial-gradient(ellipse at 50% 45%, var(--parchment-light) 0%, var(--parchment-mid) 60%, var(--parchment-dark) 100%);
  }
  .masthead__name {
    position: absolute;
    left: 0;
    top: 62px;
    width: 1200px;
    margin: 0;
    text-align: center;
    font-family: "Alegreya", Georgia, serif;
    font-weight: 700;
    font-size: 158px;
    line-height: 1;
    letter-spacing: 2px;
    color: var(--ink);
  }
  .masthead__tagline {
    position: absolute;
    left: 130px;
    top: 256px;
    width: 914px;
    display: flex;
    align-items: center;
    gap: 18px;
  }
  .masthead__rule {
    flex: 1;
    height: 2px;
    background: var(--rule);
  }
  .masthead__slogan {
    font-family: "Alegreya", Georgia, serif;
    font-weight: 700;
    font-size: 42px;
    line-height: 1;
    letter-spacing: 1px;
    color: var(--ink);
    white-space: nowrap;
  }
</style>
</head>
<body>
  <header class="masthead">
    <div class="masthead__backdrop" role="img" aria-label="Aged parchment covered with faint engraved technical diagrams of geometric figures, pulleys and a wheeled scientific instrument"></div>
    <h1 class="masthead__name">LMVBeacon</h1>
    <div class="masthead__tagline">
      <span class="masthead__rule"></span>
      <span class="masthead__slogan">All the news you need</span>
      <span class="masthead__rule"></span>
    </div>
  </header>
</body>
</html>
```